Custom Truck shop New Business Card design

double sided business card including my new logo, brand colors and picking a font I attached, clean and modern look. I attached the old card for some reference. and would like to include the picture of the white truck attached. I would also like to have it with one of my employees info as well. (same info except name and title Brenna Dulwick Service Writer)

Todd Varnell
Owner

address
20418 E Pinecrest Service Rd S
STE 310
Ashford Mesa, UT 80517

phone 720-384-9172

email todd@ironcanyonrigs.com

website ironcanyonrogs.com

social @ironcanyonrigs

Target Market(s)

men 18-60

Industry/Entity Type

Automotive

Contact Information for Business Card

Todd Varnell Owner address 20418 E Pinecrest Service Rd S STE 310 Ashford Mesa, UT 80517 phone 720-384-9172 email todd@ironcanyonrigs.com website ironcanyonrogs.com social @ironcanyonrigs

Font styles to use
Other font styles liked:
• fonts attached

Requirements
Must have
• new logo, orange #FC68D, Charcoal #333333
Nice to have
• the white truck

```html
<!DOCTYPE html>
<html lang="en">
<head>
<meta charset="utf-8">
<title>Iron Canyon Rigs – Business Card</title>
<link href="https://fonts.googleapis.com/css2?family=Jost:wght@500;700;800&display=swap" rel="stylesheet">
<style>
  :root{
    --orange:#e97240;
    --orange-light:#f3a480;
    --charcoal:#333333;
    --card-white:#f1f1f1;
    --backdrop:#cfcfcf;
    --rule:#e36a35;
  }
  *{box-sizing:border-box;margin:0;padding:0}
  html,body{width:1200px;height:1200px;overflow:hidden}
  body{
    background:var(--backdrop);
    font-family:"Jost",sans-serif;
    display:flex;flex-direction:column;align-items:center;justify-content:center;gap:60px;
  }
  .card{
    width:700px;height:400px;border-radius:26px;position:relative;
    box-shadow:0 10px 24px rgba(0,0,0,.18);
  }
  /* front */
  .card-front{
    background:linear-gradient(90deg,var(--orange-light) 0%,var(--orange) 62%,var(--orange) 100%);
    display:flex;flex-direction:column;align-items:center;
  }
  .brand{display:flex;align-items:center;gap:14px}
  .brand-dot{width:44px;height:44px;border-radius:50%;background:var(--charcoal);flex:none}
  .brand-name{font-weight:800;font-size:34px;letter-spacing:1px;color:var(--charcoal);text-transform:uppercase;white-space:nowrap}
  .card-front .brand{margin-top:150px}
  .social-handle{
    position:absolute;bottom:48px;left:0;right:0;text-align:center;
    color:#fff;font-weight:800;font-size:17px;letter-spacing:.3px;
  }
  /* back */
  .card-back{background:var(--card-white);padding:0 42px}
  .card-back .brand{position:absolute;top:48px;right:42px}
  .card-back .brand-dot{background:var(--charcoal);box-shadow:0 0 0 3px var(--orange)}
  .card-back .brand-name{font-size:28px}
  .person{position:absolute;left:42px;top:176px}
  .person-name{font-weight:800;font-size:46px;color:var(--orange);line-height:1}
  .person-title{font-weight:700;font-size:17px;color:var(--charcoal);margin-top:6px}
  .divider{position:absolute;left:42px;right:42px;top:252px;height:2px;background:var(--rule)}
  .contact{position:absolute;left:42px;right:42px;top:266px;color:var(--charcoal);font-weight:700}
  .address{font-size:16.5px;letter-spacing:.3px;white-space:nowrap}
  .contact-row{display:flex;align-items:center;gap:22px;margin-top:12px;font-size:16px}
  .contact-item{display:flex;align-items:center;gap:8px;white-space:nowrap}
  .contact-item svg{width:17px;height:17px;flex:none;fill:none;stroke:var(--orange);stroke-width:2}
  .contact-item svg .solid{fill:var(--orange);stroke:none}
</style>
</head>
<body>
  <section class="card card-front" aria-label="Card front">
    <div class="brand">
      <span class="brand-dot"></span>
      <span class="brand-name">Iron Canyon Rigs</span>
    </div>
    <p class="social-handle">@ironcanyonrigs</p>
  </section>

  <section class="card card-back" aria-label="Card back">
    <div class="brand">
      <span class="brand-dot"></span>
      <span class="brand-name">Iron Canyon Rigs</span>
    </div>

    <div class="person">
      <h1 class="person-name">Todd Varnell</h1>
      <p class="person-title">Owner</p>
    </div>

    <div class="divider"></div>

    <div class="contact">
      <p class="address">20418 E Pinecrest Service Rd S STE 310 Ashford Mesa, UT 80517</p>
      <div class="contact-row">
        <span class="contact-item">
          <svg viewBox="0 0 24 24"><path class="solid" d="M6.6 10.8a15 15 0 0 0 6.6 6.6l2.2-2.2a1 1 0 0 1 1-.25 11 11 0 0 0 3.6.6 1 1 0 0 1 1 1V20a1 1 0 0 1-1 1A17 17 0 0 1 3 4a1 1 0 0 1 1-1h3.5a1 1 0 0 1 1 1 11 11 0 0 0 .6 3.6 1 1 0 0 1-.25 1z"/></svg>
          720-384-9172
        </span>
        <span class="contact-item">
          <svg viewBox="0 0 24 24"><rect x="6" y="2" width="12" height="20" rx="2"/><circle class="solid" cx="12" cy="18" r="1.3"/></svg>
          720-593-2618
        </span>
        <span class="contact-item">
          <svg viewBox="0 0 24 24"><rect class="solid" x="2" y="5" width="20" height="14" rx="1.5"/><path d="M3 6l9 7 9-7" stroke="#fff"/></svg>
          todd@ironcanyonrigs.com
        </span>
      </div>
      <div class="contact-row">
        <span class="contact-item">
          <svg viewBox="0 0 24 24"><circle cx="12" cy="12" r="9.5"/><path d="M2.5 12h19M12 2.5c3 3 3 16 0 19M12 2.5c-3 3-3 16 0 19"/></svg>
          www.ironcanyonrogs.com
        </span>
      </div>
    </div>
  </section>
</body>
</html>
```